Fern Lusk medical cannibis cultivation company

tag - Lusk grow
Fern Lusk medical cannabis cultivation - logo is selected- can we please see bold examples with our selection. We are mainly dealing with medical companies and professionals. We would like to be stand out in the crowd with our designs. Welcome any and all attempts. Thanks

Target Market(s)

Medical and Professional

Industry/Entity Type

Medical And Science

Font styles to use
Sans Serif

Colors

Designer to choose colors to be used in the design.

Requirements
Must have
• Bright colour and be bold- Love the teal and magenta that is currently on the dark background design.
Nice to have
• shading and the 3D affect- The shadowed appearance.
Should not have
• Anything related to illegal activity or un professional manners

```html
<!DOCTYPE html>
<html lang="en">
<head>
<meta charset="utf-8">
<title>Fern Lusk – Card</title>
<link rel="stylesheet" href="https://fonts.googleapis.com/css2?family=Marcellus&display=swap">
<style>
  :root {
    --bg: #000000;
    --teal: #1fa6cb;
    --band-teal: #00a0c8;
    --plum: #3d0f45;
    --grey: #8c8c8c;
    --ring: #7a7a7a;
  }
  html, body {
    margin: 0;
    padding: 0;
    overflow: hidden;
    background: var(--bg);
  }
  .card {
    position: relative;
    width: 837px;
    height: 1200px;
    background: var(--bg);
    overflow: hidden;
    font-family: "Marcellus", sans-serif;
  }
  .brand-ring {
    position: absolute;
    left: 308px;
    top: 74px;
    width: 212px;
    height: 212px;
    border: 7px solid var(--ring);
    border-radius: 50%;
    box-sizing: border-box;
  }
  .brand-name {
    position: absolute;
    top: 326px;
    left: 0;
    width: 100%;
    margin: 0;
    text-align: center;
    font-size: 74px;
    font-weight: 400;
    letter-spacing: 2px;
    line-height: 1;
    color: var(--teal);
  }
  .tagline {
    position: absolute;
    top: 432px;
    left: 0;
    width: 100%;
    display: flex;
    align-items: center;
    justify-content: center;
    gap: 14px;
    font-size: 27px;
    letter-spacing: 3px;
    color: var(--grey);
  }
  .tagline .rule {
    width: 90px;
    height: 2px;
    background: var(--grey);
  }
  .bands {
    position: absolute;
    left: 0;
    bottom: 0;
    width: 837px;
    height: 1200px;
  }
</style>
</head>
<body>
  <div class="card">
    <div class="brand-ring"></div>
    <h1 class="brand-name">FERN LUSK</h1>
    <div class="tagline">
      <span class="rule"></span>
      <span class="tagline-text">LUSK GROW</span>
      <span class="rule"></span>
    </div>
    <svg class="bands" viewBox="0 0 837 1200" aria-hidden="true">
      <polygon class="band-plum" points="0,980 408,1077 837,1172 837,1200 0,1200" fill="var(--plum)"/>
      <polygon class="band-teal" points="408,1077 837,978 837,1172" fill="var(--band-teal)"/>
    </svg>
  </div>
</body>
</html>
```